Business Card Design

We are a flooring/granite/cabinet company
want a sleek and modern design card. Will send our logo. maybe our logo in 3d on card.
black card

Industry/Entity Type

Business

Contact Information for Business Card

Daniel Restrepo
company name Stonecrest Tile Depot
4728 loop 60w 78419
210-647-3928
stonecresttiledepot@mailbarn.net

```html
<!DOCTYPE html>
<html lang="en">
<head>
<meta charset="utf-8">
<title>Stonecrest Tile Depot — Business Card</title>
<link href="https://fonts.googleapis.com/css2?family=Exo+2:wght@300;400;600&display=swap" rel="stylesheet">
<style>
  :root {
    --navy: #0b4a6b;
    --navy-deep: #083b57;
    --paper: #ffffff;
    --backdrop: #e9e6e1;
    --ink-light: #ffffff;
  }
  * { margin: 0; padding: 0; box-sizing: border-box; }
  html, body {
    width: 1200px; height: 848px; overflow: hidden;
    background: var(--backdrop);
    font-family: "Exo 2", Arial, sans-serif;
  }
  .stage {
    position: relative; width: 1200px; height: 848px;
  }
  .card {
    position: absolute; left: 300px;
    width: 600px; height: 343px;
    border-radius: 22px; overflow: hidden;
    background: var(--paper);
    box-shadow: 0 6px 18px rgba(0,0,0,0.18);
  }
  .card--front { top: 58px; }
  .card--back { top: 447px; }

  /* Front */
  .front-band {
    position: absolute; left: 0; right: 0; bottom: 0; height: 202px;
    background: var(--navy);
  }
  .brand {
    position: absolute; left: 0; right: 0;
    display: flex; align-items: center; justify-content: center; gap: 12px;
  }
  .card--front .brand { top: 52px; }
  .brand-mark {
    width: 30px; height: 30px; background: var(--navy);
  }
  .brand-name {
    font-weight: 600; font-size: 30px; letter-spacing: 1px;
    color: var(--navy); text-transform: uppercase;
  }
  .holder-name {
    position: absolute; left: 42px; bottom: 78px;
    color: var(--ink-light); font-weight: 300; font-size: 25px; letter-spacing: 0.5px;
  }
  .contact-list {
    position: absolute; left: 300px; top: 168px;
    list-style: none; color: var(--ink-light);
    font-weight: 300; font-size: 14px;
  }
  .contact-list li {
    display: flex; align-items: center; gap: 10px; height: 25px;
  }
  .contact-icon {
    width: 18px; height: 18px; flex: none;
  }

  /* Back */
  .back-band {
    position: absolute; left: 0; right: 0; top: 0; height: 168px;
    background: var(--navy);
  }
  .card--back .brand-mark-solo {
    position: absolute; left: 285px; top: 118px;
    width: 30px; height: 30px; background: var(--paper);
  }
  .card--back .brand { top: 180px; }
  .card--back .brand-name { font-size: 34px; }
</style>
</head>
<body>
<main class="stage">
  <section class="card card--front" aria-label="Business card front">
    <div class="brand">
      <span class="brand-mark"></span>
      <span class="brand-name">Stonecrest Tile Depot</span>
    </div>
    <div class="front-band"></div>
    <p class="holder-name">Daniel Restrepo</p>
    <ul class="contact-list">
      <li>
        <svg class="contact-icon" viewBox="0 0 18 18" aria-hidden="true">
          <rect width="18" height="18" rx="3" fill="#fff"/>
          <path d="M5 4.5l2 0 1 3-1.3 1a7 7 0 0 0 2.8 2.8l1-1.3 3 1v2a1 1 0 0 1-1 1A9 9 0 0 1 4 5.5a1 1 0 0 1 1-1z" fill="var(--navy)"/>
        </svg>
        <span>210-647-3928</span>
      </li>
      <li>
        <svg class="contact-icon" viewBox="0 0 18 18" aria-hidden="true">
          <rect width="18" height="18" rx="3" fill="#fff"/>
          <path d="M9 3.5a4 4 0 0 1 4 4c0 3-4 7-4 7s-4-4-4-7a4 4 0 0 1 4-4z" fill="var(--navy)"/>
          <circle cx="9" cy="7.5" r="1.5" fill="#fff"/>
        </svg>
        <span>4728 loop 60w 78419</span>
      </li>
      <li>
        <svg class="contact-icon" viewBox="0 0 18 18" aria-hidden="true">
          <rect width="18" height="18" rx="3" fill="#fff"/>
          <rect x="3.5" y="5" width="11" height="8" fill="var(--navy)"/>
          <path d="M3.5 5l5.5 4.5 5.5-4.5" fill="none" stroke="#fff" stroke-width="1"/>
        </svg>
        <span>stonecresttiledepot@mailbarn.net</span>
      </li>
    </ul>
  </section>

  <section class="card card--back" aria-label="Business card back">
    <div class="back-band"></div>
    <span class="brand-mark-solo"></span>
    <div class="brand">
      <span class="brand-name">Stonecrest Tile Depot</span>
    </div>
  </section>
</main>
</body>
</html>
```